Steel Company / Iron Railing Business Card Template

We are a custom steel fabrication company located in Corvale, VT. In business since 1979, we recently developed a new logo, and we're looking for a business card design to help display the new logo and our business. The name of the company is Kelvane Metalcraft. The Office Phone number is (555) 555-0143. We fabricate and install custom "wrought iron" railings on our residential side, we also fabricate and erect structural steel (think cranes and steel beams in buildings) on our commercial side. Looking to get a business card template designed. Something modern, but professional. Clear and easy to read. Front should have all business and employee information including phone number(s), email address, business information, etc. back should spotlight logo.

Industry/Entity Type

Construction / Home Improvement

Contact Information for Business Card

Business information is Kelvane Metalcraft, 48 Dunmore Blvd Suite 3307, Corvale, VT 19058. Phone number is (555) 555-0143. Website is www.kelvanemetal.example Business card should be for "Paul Hendry" with the job title "Sales & Estimating" but be editable for other employees. Paul's phone number is (610) 555-0178

Colors

Designer to choose colors to be used in the design.

Requirements
Must have
• Modern Feel, Design should be sized for standard business card sizing 3.5" x 2" (88.9mm x 50.8mm)

```html
<!DOCTYPE html>
<html lang="en">
<head>
<meta charset="utf-8">
<title>Kelvane Metalcraft – Business Card</title>
<link href="https://fonts.googleapis.com/css2?family=Poppins:wght@400;500;600;700&display=swap" rel="stylesheet">
<style>
  :root {
    --page-bg: #3a3a3a;
    --card-bg: #111112;
    --brand-blue: #2c4fa8;
    --brand-red: #c4282a;
    --text-light: #f2f2f2;
    --silver: #c9c9cc;
  }
  * { margin: 0; padding: 0; box-sizing: border-box; }
  html, body {
    width: 1200px; height: 900px; overflow: hidden;
    background: var(--page-bg);
    font-family: "Poppins", sans-serif;
  }
  .sheet {
    width: 1200px; height: 900px;
    display: flex; flex-direction: column;
    align-items: center; justify-content: center; gap: 40px;
  }
  .card {
    width: 660px; height: 377px;
    background: var(--card-bg);
    border-radius: 22px;
    box-shadow: 0 14px 30px rgba(0,0,0,.45);
    position: relative;
    display: flex; align-items: center;
  }
  .card-front { padding: 0 40px 0 48px; }
  .brand-block {
    width: 300px;
    display: flex; align-items: center; gap: 14px;
  }
  .brand-dot {
    width: 22px; height: 22px; border-radius: 50%;
    background: var(--brand-red); flex: none;
  }
  .brand-name {
    color: var(--brand-blue);
    font-weight: 700; font-size: 34px; line-height: 1.1;
    text-transform: uppercase;
  }
  .divider {
    width: 2px; height: 170px;
    background: var(--brand-red);
    margin: 0 30px 0 10px;
  }
  .contact { color: var(--text-light); }
  .person-name {
    color: var(--brand-red); font-weight: 600;
    font-size: 24px; line-height: 1.1;
  }
  .person-title { font-size: 14px; margin-bottom: 18px; }
  .address { font-size: 13px; line-height: 1.45; margin-bottom: 18px; }
  .contact-list { list-style: none; font-size: 13px; line-height: 1.7; }
  .contact-list li { display: flex; align-items: center; gap: 10px; }
  .contact-list svg { width: 12px; height: 12px; fill: var(--brand-red); flex: none; }
  .card-back { justify-content: center; }
  .back-brand {
    color: var(--silver);
    font-weight: 700; font-size: 46px; line-height: 1.1;
    text-transform: uppercase; text-align: center;
    display: flex; align-items: center; gap: 18px;
  }
  .back-brand .brand-dot { background: var(--silver); width: 26px; height: 26px; }
</style>
</head>
<body>
<main class="sheet">
  <section class="card card-front" aria-label="Card front">
    <div class="brand-block">
      <span class="brand-dot"></span>
      <span class="brand-name">Kelvane<br>Metalcraft</span>
    </div>
    <div class="divider"></div>
    <div class="contact">
      <p class="person-name">Paul Hendry</p>
      <p class="person-title">Sales &amp; Estimating</p>
      <p class="address">48 Dunmore Blvd Suite 3307<br>Corvale, VT 19058</p>
      <ul class="contact-list">
        <li><svg viewBox="0 0 24 24"><path d="M6.6 10.8a15 15 0 0 0 6.6 6.6l2.2-2.2a1 1 0 0 1 1-.25 11.4 11.4 0 0 0 3.6.57 1 1 0 0 1 1 1V20a1 1 0 0 1-1 1A17 17 0 0 1 3 4a1 1 0 0 1 1-1h3.5a1 1 0 0 1 1 1c0 1.25.2 2.45.57 3.57a1 1 0 0 1-.25 1z"/></svg>(555) 555-0143</li>
        <li><svg viewBox="0 0 24 24"><path d="M2 5h20v2l-10 7L2 7z M2 9l10 7 10-7v10H2z"/></svg>info@kelvanemetal.example</li>
        <li><svg viewBox="0 0 24 24"><circle cx="12" cy="12" r="10"/></svg>www.kelvanemetal.example</li>
      </ul>
    </div>
  </section>
  <section class="card card-back" aria-label="Card back">
    <div class="back-brand">
      <span class="brand-dot"></span>
      <span>Kelvane<br>Metalcraft</span>
    </div>
  </section>
</main>
</body>
</html>
```